Bref créative
Bellquist law p.a.
See logo attached
Simple
Hal Bellquist
Board Certified Trial Lawyer
Post Office Box 48716
27 West Caldera Street
Brindlecove, Westmere. 30874
Hal@bellquistlegal.example
Www.halbellquist.example
Here is a version with a slight varation in the size of bellquist law
Here is the final version of the logo with the bellquist law text included with the font that I though was most suitable. There is a white outline on this version that is not on the final version. It is a tif file that will not upload to this server but is on my facebook page. I can email it privately if someone needs it. I think this logo may look better on grey paper. The black background that I have in this attachment may not be feasible since it would require three colors on the letterhead. Anyway, thanks for your help.

```html
<!DOCTYPE html>
<html lang="en">
<head>
<meta charset="utf-8">
<title>Bellquist Law, P. A. — Letterhead</title>
<link rel="stylesheet" href="https://fonts.googleapis.com/css2?family=PT+Sans+Narrow:wght@400;700&display=swap">
<style>
  :root {
    --paper: #ffffff;
    --ink: #111111;
    --ink-soft: #3a3a3a;
    --accent: #e8742a;
    --frame: #4a4a4a;
    --reverse: #ffffff;
  }
  * { margin: 0; padding: 0; box-sizing: border-box; }
  html, body {
    width: 1200px;
    height: 542px;
    overflow: hidden;
    background: var(--paper);
  }
  .letterhead {
    position: relative;
    width: 1200px;
    height: 542px;
    background: var(--paper);
    font-family: "PT Sans Narrow", "Arial Narrow", sans-serif;
  }
  .letterhead__sheet {
    position: absolute;
    left: 12px;
    top: 12px;
    width: 1180px;
    height: 512px;
    border: 2px solid var(--frame);
    overflow: hidden;
  }
  .letterhead__corner {
    position: absolute;
    inset: 0;
    width: 100%;
    height: 100%;
  }
  .corner__band { fill: var(--ink); }
  .corner__stripe { fill: var(--accent); }
  .brand {
    position: absolute;
    left: 40px;
    top: 142px;
    display: flex;
    align-items: center;
    gap: 12px;
  }
  .brand__dot {
    width: 26px;
    height: 26px;
    border-radius: 50%;
    background: var(--accent);
  }
  .brand__name {
    font-size: 17px;
    font-weight: 700;
    color: var(--ink-soft);
    letter-spacing: 0.3px;
  }
  .sender-address {
    position: absolute;
    right: 12px;
    top: 42px;
    font-style: normal;
    text-align: right;
    color: var(--reverse);
    font-size: 17px;
    font-weight: 700;
    line-height: 21px;
  }
</style>
</head>
<body>
  <main class="letterhead">
    <div class="letterhead__sheet">
      <svg class="letterhead__corner" viewBox="0 0 1176 508" preserveAspectRatio="none" aria-hidden="true">
        <path class="corner__stripe" d="M814 0 Q 900 175 1176 242 L1176 228 Q 918 168 834 0 Z"/>
        <path class="corner__band" d="M834 0 Q 918 168 1176 228 L1176 0 Z"/>
      </svg>

      <div class="brand">
        <span class="brand__dot"></span>
        <span class="brand__name">Bellquist Law, P. A.</span>
      </div>

      <address class="sender-address">
        Post Office Box 48716<br>
        27 West Caldera Street<br>
        Brindlecove, Westmere 30874
      </address>
    </div>
  </main>
</body>
</html>
```